Flyer for an pediatric sleep consultancy - to distribute to play and childcare centers etc.

I need a flyer that will attract the attention of parents with children between the age of babies to toddlers, who may be experiencing sleep issues. The flyer will be placed at places such as community centers, doctors room, play centers, kindergardens, etc.

My company is called "The Quiet Meadow Studio" and provides a sleep consultancy service. My service essentially provides a customized plan for parents to follow and general advice and guidance. It is not medical advice.

I like to the flyer to have an overall tone that is soft and peaceful with a clean and beautiful design, however can catch the attention of parents who may be struggling with their child's sleep issues and are sleep deprived. I would like photos with minimal text. The colour I use is a brownish rose. I will attach some of my designs to give you an idea. You can have a look at my homepage as well to get an idea about my esthetic direction and the colour. Although the colour of my page is a bit too brownish....

I will provide the text to appear in the flyer once I have a better idea of the layout that I prefer for the flyer. The text however wont be extensive, just some catchy points.

I want to direct people to my website which is www.quietmeadowstudio-example.com
I offer a first FREE evaluation call, to the parents, to get to know each other better, learn about their child's particular sleep problems and see if we are a good fit and can work together. I would like to have this information somehow on the flyer, so that the parents will contact me.
I also have a facebook page, which is: The Quiet Meadow Studio

I have a logo that I would like to appear on the flyer. I will attach the file once the uploader on art bazaar is fixed.

When I print the flyer - I like to print A5 SIZE ... please make sure the formatting is OK for this size.

Here are some text ideas. of course all of it would be too much, I guess. On the front of the flyer I would like to have some catchy phrase or something similar to get people interested and to want to know more. On the back there could be a bit more text and information. But I'm open too suggestions....
I'm not too sure about the wording yet. But here are some text that I might be use:

Is sleep an issue in your home?

Is your baby having trouble sleeping? ... are you?!
I can help!

Sleep, baby, sleep….

Teaching children how to sleep

The Quiet Meadow Studio is a pediatric sleep consultancy that specializes in helping parents with children who struggle to develop good and healthy sleep habits.
Disruptive sleep patterns or not enough sleep can affect the physical, mental and emotional development of your child.

Of course nobody plans to have a sleep problem, but habits can become easily ingrained and spiral quickly out of control and you can find yourself sleep deprived, desperate and not too sure what to do. You see all the other sleeping babies and wish there was someone who understood what you were going through?! Well, there is!

Contact me for a free 15 minute consultation.

This 15 minute „mini“ consultation is a chance to discuss your unique sleep challenges and sleep goals with me. I will provide you with an overview of how I will work with your family to achieve your wildest sleep dreams (goals).
Furthermore do I understand and believe that every child and their family is unique and there is no one size fits all!
I would love to have a chat with you and talk about how I can help make things easier for you and your family!

Do I need a sleep consultant for my child?
The answer is yes if:
- if your child will only fall asleep when nursing or bottle feeding
- if your child needs a dummy or other external aid, like being rocked, patted or taken for a care ride to fall asleep
- if your good night routine is a challenging and exhausting procedure instead of a relaxed and enjoyable moment for the whole family
- if sleep is a constant battle in your home which leaves you feeling frustrated and exhausted
- if your own lack of sleep is taking a toll on you and the whole family

What can I do for you?

I will:

- Guide you to set an age appropriate foundation for good sleep
- Create an individual sleep plan tailored especially to your child’s sleep needs and circumstances
- Help you to teach your childto go to sleep and get back to sleep independently during the night
- show you how to teach your child to take healthful, restorative naps
-Learn

Contact:

Marta Lindqvist
info@quietmeadowstudio-example.com
www.quietmeadowstudio-example.com
+34 612 380 574

Consultations in English, German or Spanish via Phone/Skype or home consultation

Reason: I have to go on a business trip and won't be able to choose a design until the deadline. During the trip I won't have time to give feedback and ask for changes. thank you

Target Market(s)

parents, sleep deprived mothers, young families, child care provider,

Industry/Entity Type

Baby Care

Contact Information for Business Card

Marta Lindqvist
pediatric sleep consultant
+34 612 380 574

```html
<!DOCTYPE html>
<html lang="en">
<head>
<meta charset="utf-8">
<title>The Quiet Meadow Studio – Flyer</title>
<link href="https://fonts.googleapis.com/css2?family=Quicksand:wght@400;500;600&family=Parisienne&family=Open+Sans:wght@600;700&display=swap" rel="stylesheet">
<style>
:root{
  --backdrop:#4a4a4a;
  --rose:#c88f82;
  --rose-deep:#b57a6d;
  --rose-soft:#d9a99c;
  --peach:#f8e1d6;
  --peach-light:#fcefe8;
  --sage:#93a49f;
  --ink:#7b716d;
  --ink-soft:#9c918d;
  --white:#ffffff;
}
*{margin:0;padding:0;box-sizing:border-box}
html,body{width:1200px;height:871px;overflow:hidden;background:var(--backdrop)}
body{position:relative;font-family:'Quicksand',sans-serif}
.page{position:absolute;top:77px;width:494px;height:712px;overflow:hidden;background:var(--white)}
.page--front{left:70px}
.page--back{left:611px;background:var(--rose)}
.abs{position:absolute}
.script{font-family:'Parisienne',cursive}
.photo{position:absolute}

/* front */
.front-photo{left:0;top:0;width:494px;height:335px;background:linear-gradient(180deg,#fbfaf9 0%,#f1edeb 45%,#e4dcd8 100%)}
.brand{left:18px;top:78px;color:var(--ink);font-size:20px;font-weight:500;display:flex;align-items:center;gap:8px}
.brand-dot{width:14px;height:14px;border-radius:50%;background:var(--rose-soft)}
.brand-by{left:150px;top:106px;color:var(--ink-soft);font-size:12px;font-weight:500}
.tagline{right:14px;top:22px;width:170px;text-align:right;color:#a7a3a2;font-size:31px;line-height:1.05}
.hook{left:96px;top:222px;color:var(--rose-soft);font-size:24px}
.hook-big{left:34px;top:252px;color:var(--rose);font-size:38px}
.front-band{left:0;top:335px;width:266px;height:377px;background:var(--rose)}
.front-col{left:266px;top:335px;width:228px;height:377px;background:var(--peach)}
.help-box{left:23px;top:335px;width:193px;height:150px;background:radial-gradient(circle at 30% 40%,#fff6ee 0%,#f9d9c4 55%,#eebfa6 100%);text-align:center;color:var(--ink);padding-top:14px;box-shadow:0 0 0 3px rgba(255,255,255,.4)}
.help-box p{font-size:19px;line-height:1.15}
.help-box .are{font-size:28px;margin-top:2px}
.help-box .can{font-family:'Open Sans',sans-serif;font-weight:700;color:var(--rose-deep);font-size:24px;margin-top:8px}
.offer{left:288px;top:277px;width:128px;height:128px;border-radius:50%;background:var(--rose-soft);border:4px solid var(--peach-light);color:var(--white);font-family:'Open Sans',sans-serif;font-weight:700;font-size:15px;line-height:1.2;display:flex;align-items:center;justify-content:center;text-align:center}
.body-white{left:20px;top:508px;width:232px;color:var(--white);font-size:8.4px;line-height:1.45}
.body-white p{margin-bottom:7px}
.body-dark{left:282px;top:430px;width:198px;color:var(--ink);font-size:8.4px;line-height:1.45}
.body-dark p{margin-bottom:7px}
.contact{left:282px;top:618px;width:200px;text-align:right}
.contact-name{color:var(--rose);font-size:14px;font-weight:500}
.contact-name em{font-size:11px;font-weight:600}
.contact-mail{color:var(--rose-deep);font-size:10px;font-weight:600;margin-top:2px}
.contact-phone{color:var(--rose-deep);font-family:'Open Sans',sans-serif;font-weight:700;font-size:21px;margin-top:8px;text-align:left}

/* back */
.hero-photo{left:17px;top:28px;width:280px;height:136px;border:5px solid #f1e6dc;background:linear-gradient(135deg,#fbf6f2,#eedfd5 60%,#d9bfb1)}
.q-title{left:22px;top:180px;color:var(--white);font-size:13.5px;font-weight:500}
.q-sub{left:22px;top:198px;color:var(--white);font-size:9px}
.bullets{list-style:none;color:var(--white);font-size:7.6px;line-height:1.35}
.bullets li{position:relative;padding-left:18px;margin-bottom:8px}
.bullets li::before{content:"";position:absolute;left:2px;top:1px;width:8px;height:8px;border-radius:50%;background:#8a6259}
.bullets--answer{position:absolute;left:22px;top:215px;width:270px}
.w-title{left:318px;top:22px;color:var(--white);font-size:13.5px;font-weight:500}
.w-sub{left:318px;top:42px;color:var(--white);font-size:8px}
.bullets--offer{position:absolute;left:318px;top:58px;width:165px}
.small-photo{left:311px;top:237px;width:166px;height:116px;border:5px solid #f0e7e2;background:linear-gradient(160deg,#ffffff,#f3e6e0 60%,#dcc3b7)}
.sage-block{left:0;top:367px;width:494px;height:245px;background:var(--sage)}
.call-text{left:22px;top:388px;width:190px;color:var(--white);font-family:'Open Sans',sans-serif;font-weight:600;font-size:19.5px;line-height:1.4}
.call-text p+p{margin-top:12px}
.crib-photo{left:210px;top:367px;width:270px;height:245px;background:linear-gradient(180deg,#e5e1dc,#cfc9c2 55%,#b9b0a8)}
.social{left:345px;top:536px;width:88px;text-align:center;color:var(--white);font-size:8px;font-weight:600;line-height:1.2}
.social-square{width:22px;height:22px;background:var(--rose);margin:0 auto 4px}
.phone-band{left:0;top:582px;width:232px;height:34px;background:var(--rose-soft);color:var(--white);font-family:'Open Sans',sans-serif;font-weight:600;font-size:20px;padding:3px 0 0 20px;display:flex;align-items:center;gap:8px}
.foot{left:0;top:612px;width:494px;height:100px;background:var(--white)}
.mail-band{left:0;top:616px;width:262px;height:22px;background:var(--rose);color:var(--white);font-size:8px;font-weight:600;padding:6px 0 0 22px}
.site{left:18px;top:668px;color:var(--rose);font-size:19px;font-weight:500}
.brand-back{right:22px;top:640px;color:var(--ink);font-size:15px;font-weight:500;text-align:right}
.brand-back span{display:block;color:var(--ink-soft);font-size:10px;margin-top:3px}
</style>
</head>
<body>

<section class="page page--front">
  <div class="photo front-photo" role="img" aria-label="Photo of a baby sleeping in a white crib"></div>
  <div class="abs brand"><span class="brand-dot"></span>The Quiet Meadow Studio</div>
  <div class="abs brand-by">by Marta Lindqvist</div>
  <div class="abs tagline script">Teaching Children How to Sleep</div>
  <div class="abs hook script">Is sleep an issue in your home?</div>
  <div class="abs hook-big script">Sleep Baby Sleep</div>

  <div class="abs front-band"></div>
  <div class="abs front-col"></div>

  <div class="abs help-box">
    <p>Is your baby having<br>trouble sleeping?...</p>
    <p class="are">Are you?!</p>
    <p class="can">I can help!</p>
  </div>

  <div class="abs offer">Contact me<br>for a FREE<br>15 Minute<br>Consultation</div>

  <div class="abs body-white">
    <p>The Quiet Meadow Studio is a pediatric sleep consultancy that specializes in helping parents with children who struggle to develop good and healthy sleep habits.</p>
    <p>Disruptive sleep patterns or not enough sleep can affect the physical, mental and emotional development of your child.</p>
    <p>Of course nobody plans to have a sleep problem, but habits can become easily ingrained and spiral quickly out of control and you can find yourself sleep deprived, desperate and not too sure what to do. You see all the other sleeping babies and wish there was someone who understood what you were going through?! Well, there is!</p>
  </div>

  <div class="abs body-dark">
    <p>This 15 minute 'mini' consultation is a chance to discuss your unique sleep challenges and sleep goals with me. I will provide you with an overview of how I will work with your family to achieve your wildest sleep dreams (goals).</p>
    <p>Furthermore do I understand and believe that every child and their family is unique and there is no one size fits all!</p>
    <p>I would love to have a chat with you and talk about how I can help make things easier for you and your family!</p>
  </div>

  <div class="abs contact">
    <div class="contact-name"><em>Contact me:</em> Marta Lindqvist</div>
    <div class="contact-mail">info@quietmeadowstudio-example.com</div>
    <div class="contact-phone">+34 612 380 574</div>
  </div>
</section>

<section class="page page--back">
  <div class="photo hero-photo" role="img" aria-label="Photo of a mother sleeping beside her baby"></div>

  <div class="abs q-title">Do I need a sleep consultant for my child?</div>
  <div class="abs q-sub">THE ANSWER IS YES IF:</div>
  <ul class="bullets bullets--answer">
    <li>If your child will only fall asleep when nursing or bottle feeding</li>
    <li>If your child needs a dummy or other external aid, like being rocked, patted or taken for a care ride to fall asleep</li>
    <li>If your good night routine is a challenging and exhausting procedure instead of a relaxed and enjoyable moment for the whole family</li>
    <li>If sleep is a constant battle in your home which leaves you feeling frustrated and exhausted</li>
    <li>If your own lack of sleep is taking a toll on you and the whole family</li>
  </ul>

  <div class="abs w-title">What can I do for you?</div>
  <div class="abs w-sub">I will:</div>
  <ul class="bullets bullets--offer">
    <li>Guide you to set an age appropriate foundation for good sleep</li>
    <li>Create an individual sleep plan tailored especially to your child's sleep needs and circumstances</li>
    <li>Help you to teach your child to go to sleep and get back to sleep independently during the night</li>
    <li>Show you how to teach your child to take healthful, restorative naps</li>
    <li>Learn</li>
  </ul>

  <div class="photo small-photo" role="img" aria-label="Photo of a toddler asleep on a white blanket"></div>

  <div class="abs sage-block"></div>
  <div class="abs call-text">
    <p>Do I need a sleep consultant for my child?</p>
    <p>If answer is YES, Please call me</p>
  </div>
  <div class="photo crib-photo" role="img" aria-label="Photo of a toddler standing at a white crib beside a star cushion"></div>
  <div class="abs social"><div class="social-square"></div>THE QUIET MEADOW STUDIO</div>

  <div class="abs foot"></div>
  <div class="abs phone-band">
    <svg width="14" height="14" viewBox="0 0 24 24" aria-hidden="true"><path fill="#fff" d="M6.6 10.8a15.1 15.1 0 0 0 6.6 6.6l2.2-2.2c.3-.3.7-.4 1-.2 1.1.4 2.3.6 3.6.6.6 0 1 .4 1 1V20c0 .6-.4 1-1 1A17 17 0 0 1 3 4c0-.6.4-1 1-1h3.5c.6 0 1 .4 1 1 0 1.3.2 2.5.6 3.6.1.3 0 .7-.2 1z"/></svg>
    +34 612 380 574
  </div>
  <div class="abs mail-band">Marta Lindqvist: info@quietmeadowstudio-example.com</div>
  <div class="abs site">quietmeadowstudio-example.com</div>
  <div class="abs brand-back">The Quiet Meadow Studio<span>by Marta Lindqvist</span></div>
</section>

</body>
</html>
```